Brisk Hollow Builders Needs A Flyer

We need a flyer for our newest product "The Cedarlane Garden Workroom"

Here is some copy for the flyer:

1. More and more people everyday are working from home and finding it difficult to disconnect from home activities in order to focus on their work. They are also finding it very expensive to add on to their existing house for a quiet place. Our archatectually stunning, Cedarlane Garden Workroom is the answer. The office studio measures 16' wide and 10' deep. 160 Square feet of space.

Perfect for dozens of purposes. Home office, design studio, artist studio, home school office, reading room, craft studio, drafting room.

Features include:

- Steel Framing. 40-60% lighter then wood, higher strength to weight ratio, resistant to mold and fire and steel is the most recycled material on earth!
- Spray foam insulation. Cool in the summer and warm in the winter.
- HVAC Mini Split with wireless remote control and thermostat.
- 100% Off grid with enough solar and battery storage to run your entire office. No need to pay for an expensive electric installation.
- Flush fitting floor outlets to reduce wires.
- TV mount (Optional with pre-wired electric, HDMI, digital audio & Cat 6)
- Windows are tempered glass custom made by Morvik Glazing.
- Solar qualifies for a 26% tax credit. This is not a write-off rather it is a direct reduction on your tax obligation.
- Thousands of dollars less than adding onto your home.
- Custom color, siding, features available.

This beautiful back yard office is delivered 100% assembled and ready to enjoy on the day of delivery.

We ship nationwide from our factory in South Carolina. Give us a call anytime to speak to a designer and start your dream office today!

555-318-4027
info@BriskHollowBuilders.example

```html
<!DOCTYPE html>
<html lang="en">
<head>
<meta charset="utf-8">
<title>The Cedarlane Garden Workroom – Brisk Hollow Builders</title>
<link rel="stylesheet" href="https://fonts.googleapis.com/css2?family=Roboto:wght@400;500;700;900&display=swap">
<style>
  :root {
    --magenta: #c4176c;
    --purple: #4a1f6e;
    --body-purple: #6a1b6f;
    --grey: #4a4a4a;
    --ink: #1e1e1e;
    --green: #1ea64b;
    --lime: #8cc63f;
    --yellow: #f4e21c;
    --teal: #0f7f73;
    --white: #ffffff;
  }
  * { box-sizing: border-box; margin: 0; padding: 0; }
  html, body { width: 855px; height: 1200px; overflow: hidden; background: var(--white); }
  body { font-family: "Roboto", Arial, sans-serif; color: var(--grey); }
  .flyer { position: relative; width: 855px; height: 1200px; overflow: hidden; background: var(--white); }
  .art { position: absolute; inset: 0; width: 855px; height: 1200px; }

  .brand {
    position: absolute; left: 530px; top: 150px; width: 270px;
    display: flex; align-items: center; gap: 10px;
    font-weight: 900; font-size: 27px; line-height: 1.05; color: var(--green);
    text-transform: uppercase; letter-spacing: 0.5px;
  }
  .brand-dot { flex: none; width: 22px; height: 22px; border-radius: 50%; background: var(--yellow); }

  .title {
    position: absolute; right: 40px; top: 232px; text-align: right;
    color: var(--magenta); font-weight: 700;
  }
  .title .lead { display: block; font-size: 34px; line-height: 44px; }
  .title .main { display: block; font-size: 39px; line-height: 44px; }

  .features-heading {
    position: absolute; left: 591px; top: 339px;
    font-size: 29px; line-height: 36px; font-weight: 700; color: var(--purple);
  }
  .features { position: absolute; left: 433px; top: 0; width: 398px; height: 1200px; list-style: none; }
  .features li {
    position: absolute; left: 0; right: 0; padding-left: 21px;
    font-size: 18.5px; line-height: 22.4px; color: var(--grey); text-align: justify;
  }
  .features li::before {
    content: ""; position: absolute; left: 0; top: 4px;
    border-top: 7px solid transparent; border-bottom: 7px solid transparent;
    border-right: 12px solid var(--purple);
    transform: rotate(45deg);
  }
  .features .f-framing { top: 387px; }
  .features .f-insulation { top: 489px; }
  .features .f-hvac { top: 562px; }
  .features .f-offgrid { top: 629px; }
  .features .f-outlets { top: 739px; }
  .features .f-tv { top: 784px; }
  .features .f-windows { top: 858px; }
  .features .f-tax { top: 928px; }
  .features .f-savings { top: 1016px; }
  .features .f-custom { top: 1080px; }

  .intro {
    position: absolute; left: 28px; top: 521px; width: 363px;
    font-size: 18px; line-height: 22.4px; color: var(--body-purple); text-align: justify;
  }
  .purposes {
    position: absolute; left: 0; top: 765px; width: 398px; height: 80px;
    background: var(--magenta); color: var(--white);
    padding: 4px 12px 0 28px; font-size: 16px; font-weight: 700; line-height: 22px;
  }
  .delivery {
    position: absolute; left: 28px; top: 861px; width: 360px;
    font-size: 19px; line-height: 23px; color: var(--ink);
  }
  .shipping {
    position: absolute; left: 110px; top: 971px; width: 275px; text-align: center;
    font-size: 16px; line-height: 22px; color: var(--ink);
  }
  .shipping p + p { margin-top: 15px; }

  .phone {
    position: absolute; left: 62px; top: 1136px;
    display: flex; align-items: center; gap: 8px;
    font-size: 32px; font-weight: 700; color: var(--ink);
  }
  .contact {
    position: absolute; left: 545px; top: 1128px; list-style: none;
    font-size: 15.5px; font-weight: 700; color: var(--white); line-height: 24px;
  }
  .contact li { display: flex; align-items: center; gap: 10px; }
</style>
</head>
<body>
<main class="flyer">
  <svg class="art" viewBox="0 0 855 1200">
    <defs>
      <linearGradient id="band" x1="1" y1="0" x2="0" y2="1">
        <stop offset="0" stop-color="#1ea64b"/>
        <stop offset="0.6" stop-color="#8cc63f"/>
        <stop offset="1" stop-color="#f4e21c"/>
      </linearGradient>
      <linearGradient id="footer" x1="0" y1="0" x2="1" y2="0">
        <stop offset="0" stop-color="#f4e21c"/>
        <stop offset="0.45" stop-color="#6dbd45"/>
        <stop offset="1" stop-color="#0f7f73"/>
      </linearGradient>
      <linearGradient id="accent" x1="0" y1="0" x2="1" y2="1">
        <stop offset="0" stop-color="#f4e21c"/>
        <stop offset="0.5" stop-color="#8cc63f"/>
        <stop offset="1" stop-color="#1ea64b"/>
      </linearGradient>
      <linearGradient id="photoTop" x1="0" y1="0" x2="0" y2="1">
        <stop offset="0" stop-color="#7f9a6e"/>
        <stop offset="0.55" stop-color="#3d4a3e"/>
        <stop offset="1" stop-color="#6f8f4a"/>
      </linearGradient>
      <linearGradient id="photoBottom" x1="0" y1="0" x2="0" y2="1">
        <stop offset="0" stop-color="#b9cfd9"/>
        <stop offset="0.5" stop-color="#4c5156"/>
        <stop offset="1" stop-color="#6f9a48"/>
      </linearGradient>
    </defs>

    <polygon role="img" aria-label="Photo of the garden workroom with glass doors among trees"
             points="0,0 548,0 358,258 0,258" fill="url(#photoTop)"/>
    <polygon role="img" aria-label="Photo of the workroom from the side with solar panels on the roof"
             points="0,279 400,279 322,390 245,500 0,500" fill="url(#photoBottom)"/>
    <polygon points="548,0 592,0 336,345 292,345" fill="url(#band)"/>

    <polygon class="accent-mid" role="img" aria-label="Decorative green and yellow pattern"
             points="340,345 430,345 430,455 380,505 300,455" fill="url(#accent)"/>
    <polygon class="accent-corner" role="img" aria-label="Decorative green and yellow pattern"
             points="0,943 135,943 135,1085 90,1118 0,1118" fill="url(#accent)"/>

    <polygon points="0,1134 855,1110 855,1200 0,1200" fill="url(#footer)"/>
  </svg>

  <div class="brand"><span class="brand-dot"></span><span>Brisk Hollow Builders</span></div>

  <h1 class="title">
    <span class="lead">The Cedarlane Garden</span>
    <span class="main">Workroom</span>
  </h1>

  <h2 class="features-heading">Features</h2>
  <ul class="features">
    <li class="f-framing">Steel Framing. 40-60% lighter then wood, higher strength to weight ratio, resistant to mold and fire and steel is the most recycled material on earth!</li>
    <li class="f-insulation">Spray foam insulation. Cool in the summer and warm in the winter.</li>
    <li class="f-hvac">HVAC Mini Split with wireless remote control and thermostat.</li>
    <li class="f-offgrid">100% Off grid with enough solar and battery storage to run your entire office. No need to pay for an expensive electric installation.</li>
    <li class="f-outlets">Flush fitting floor outlets to reduce wires.</li>
    <li class="f-tv">TV mount (Optional with pre-wired electric, HDMI, digital audio &amp; Cat 6)</li>
    <li class="f-windows">Windows are tempered glass custom made by Morvik Glazing.</li>
    <li class="f-tax">Solar qualifies for a 26% tax credit. This is not a write-off rather it is a direct reduction on your tax obligation.</li>
    <li class="f-savings">Thousands of dollars less than adding onto your home.</li>
    <li class="f-custom">Custom color, siding, features available</li>
  </ul>

  <p class="intro">More and more people everyday are working from home and finding it difficult to disconnect from home activities in order to focus on their work. They are also finding it very expensive to add on to their existing house for a quiet place. Our archatectually stunning, Cedarlane Garden Workroom is the answer. The office studio measures 16' wide and 10' deep. 160 Square feet of space.</p>

  <p class="purposes">Perfect for dozens of purposes. Home office, design studio, artist studio, home school office, reading room, craft studio, drafting room.</p>

  <p class="delivery">This beautiful back yard office is delivered 100% assembled and ready to enjoy on the day of delivery.</p>

  <div class="shipping">
    <p>We ship nationwide from our factory in South Carolina.</p>
    <p>Give us a call anytime to speak to a designer and start your dream office today!</p>
  </div>

  <div class="phone">
    <svg width="30" height="30" viewBox="0 0 24 24" aria-hidden="true"><path fill="#1ea64b" d="M6.6 10.8a15.1 15.1 0 0 0 6.6 6.6l2.2-2.2a1 1 0 0 1 1-.25 11.4 11.4 0 0 0 3.6.57 1 1 0 0 1 1 1V20a1 1 0 0 1-1 1A17 17 0 0 1 3 4a1 1 0 0 1 1-1h3.5a1 1 0 0 1 1 1c0 1.250.2 2.450.57 3.570a1 1 0 0 1-.25 1z"/></svg>
    <span>555-318-4027</span>
  </div>

  <ul class="contact">
    <li><svg width="16" height="12" viewBox="0 0 16 12" aria-hidden="true"><rect x="0.75" y="0.75" width="14.5" height="10.5" fill="none" stroke="#fff" stroke-width="1.5"/><polyline points="1,1 8,7 15,1" fill="none" stroke="#fff" stroke-width="1.5"/></svg>info@BriskHollowBuilders.example</li>
    <li><svg width="16" height="16" viewBox="0 0 16 16" aria-hidden="true"><circle cx="8" cy="8" r="7" fill="none" stroke="#fff" stroke-width="1.5"/><ellipse cx="8" cy="8" rx="3" ry="7" fill="none" stroke="#fff" stroke-width="1.2"/><line x1="1" y1="8" x2="15" y2="8" stroke="#fff" stroke-width="1.2"/></svg>www.briskhollowbuilders.example</li>
  </ul>
</main>
</body>
</html>
```